Attract renters to our neighborhoods - inform renters who we are

Apartments in several neighborhoods. We want to attract renters who want to live along the lake or other near by neighborhoods. We want them to know that we have an apartment for them in their location.
The perfect location to spend your time.
When minutes matter LIVE where you work and play! (love this tag line)
Updates

www.kvtresidences.example Choose from over 3,700 apartments in Chicago’s most celebrated neighborhoods. 773-582-6041 Chicago’s most celebrated neighborhoods. 31 PROPERTIES

Target Market(s)

Sophisticated apartment renter who wants location, space, amenities

Industry/Entity Type

Apartment Rentals

Requirements
Must have
• Feel like I want to live there, or the ad is calling me
Nice to have
• Appeal to a sophisticated apartment renter. We have what you want, where you want to be.
Should not have
• Logo colors are black and red/burnt orange see attached logo

```html
<!DOCTYPE html>
<html lang="en">
<head>
<meta charset="utf-8">
<title>KVT Residences Flyer</title>
<link rel="stylesheet" href="https://fonts.googleapis.com/css2?family=Archivo:wght@600;700;800;900&family=Montserrat:wght@400;500;600;700;800&display=swap">
<style>
:root{
  --red:#c0272d;
  --black:#0b0b0b;
  --white:#ffffff;
  --ink:#222222;
  --page:#efefef;
}
*{margin:0;padding:0;box-sizing:border-box}
html,body{width:783px;height:1200px;overflow:hidden;background:var(--page)}
.flyer{position:absolute;left:16px;top:69px;width:751px;height:1062px;background:var(--white);box-shadow:0 4px 14px rgba(0,0,0,.18);overflow:hidden;font-family:'Montserrat',sans-serif;color:var(--ink)}
.hero{position:absolute;left:0;top:0;width:751px;height:475px}
.brand{position:absolute;left:48px;top:50px;font-family:'Archivo',sans-serif;font-weight:900;font-size:82px;line-height:1;color:var(--black);letter-spacing:-2px}
.headline{position:absolute;left:48px;top:158px;font-family:'Archivo',sans-serif;font-weight:800;line-height:1;text-transform:uppercase;white-space:nowrap}
.headline span{display:block}
.headline .small{font-family:'Montserrat',sans-serif;font-weight:600;font-size:31px;color:var(--black);margin-bottom:4px}
.headline .red{color:var(--red)}
.headline .l2{font-size:48px;letter-spacing:-1px}
.headline .l3{font-size:34.5px;color:var(--black);margin-top:4px;letter-spacing:-.3px}
.headline .l4{font-size:58px;letter-spacing:-1px;margin-top:2px}
.band-text{position:absolute;left:50px;top:372px;font-weight:700;font-size:21px;line-height:27px;color:var(--white);letter-spacing:.3px}
.section-title{font-family:'Archivo',sans-serif;font-weight:800;font-size:17.8px;text-transform:uppercase;color:var(--black);letter-spacing:-.2px;white-space:nowrap}
.section-title em{font-style:normal;color:var(--red)}
.copy{font-size:11.3px;line-height:13.6px;text-align:justify;color:#333}
.intro{position:absolute;left:46px;top:490px;width:650px}
.intro .copy{margin-top:8px}
.explore{position:absolute;left:70px;top:600px;width:614px;display:flex;align-items:center;gap:12px}
.explore .rule{flex:1;height:2px;background:linear-gradient(90deg,transparent,#333,#333)}
.explore .rule.right{background:linear-gradient(90deg,#333,#333,transparent)}
.hoods{position:absolute;left:48px;top:638px;display:flex;gap:22px}
.hood{width:148px;text-align:center}
.hood .photo{width:148px;height:122px;box-shadow:0 1px 4px rgba(0,0,0,.35);border:2px solid #fff}
.hood .name{margin-top:14px;font-family:'Archivo',sans-serif;font-weight:600;font-size:14px;color:var(--black);white-space:nowrap;letter-spacing:-.2px}
.hood .underline{width:36px;height:2px;background:var(--red);margin:7px auto 0}
.celebrated{position:absolute;left:46px;top:820px;width:650px}
.celebrated .section-title{line-height:25px}
.celebrated .copy{margin-top:6px}
.footer{position:absolute;left:0;top:965px;width:751px;height:97px}
.contact{position:absolute;left:50px;top:988px;color:var(--white);font-weight:700}
.contact div{display:flex;align-items:center;gap:7px}
.contact .phone{font-size:21px;letter-spacing:.3px}
.contact .line{font-size:12.5px;margin-top:3px}
.contact svg{flex:none}
.follow{position:absolute;left:340px;top:1019px;color:var(--white);font-weight:700;font-size:7.5px}
.follow .chips{display:flex;gap:4px;margin-top:3px}
.follow .chips i{display:block;width:14px;height:14px;border:2px solid var(--white);border-radius:3px}
.partners{position:absolute;left:476px;top:988px}
.partners .label{font-weight:700;font-size:13px;color:var(--black)}
.partners .badges{display:flex;align-items:center;gap:14px;margin-top:8px}
.badge{display:block}
</style>
</head>
<body>
<div class="flyer">
  <svg class="hero" viewBox="0 0 751 475" width="751" height="475">
    <defs>
      <linearGradient id="skyline" x1="0" y1="0" x2="0" y2="1">
        <stop offset="0" stop-color="#b9d1e4"/>
        <stop offset=".25" stop-color="#8fb5d0"/>
        <stop offset=".32" stop-color="#3d7ea8"/>
        <stop offset=".55" stop-color="#5b7f92"/>
        <stop offset=".8" stop-color="#8d8f86"/>
        <stop offset="1" stop-color="#6f7d63"/>
      </linearGradient>
    </defs>
    <rect x="0" y="0" width="751" height="475" fill="url(#skyline)" role="img" aria-label="Aerial view of downtown Chicago towers by the lake with a hand holding a phone"/>
    <polygon points="0,0 258,0 573,475 0,475" fill="var(--white)"/>
    <polygon points="0,355 493,355 573,475 0,475" fill="var(--black)"/>
    <polygon points="584,475 751,238 751,475" fill="var(--white)"/>
    <polygon points="598,475 751,260 751,475" fill="var(--red)"/>
  </svg>

  <div class="brand">KVT</div>

  <h1 class="headline">
    <span class="small">When minutes</span>
    <span class="red l2">Matter live</span>
    <span class="l3">Where you work</span>
    <span class="red l4">And play!</span>
  </h1>

  <p class="band-text">Choose from over 3,700 apartments<br>in Chicago’s most celebrated<br>neighborhoods.</p>

  <section class="intro">
    <h2 class="section-title"><em>Rent a KVT apartment and</em> get a great lifestyle!</h2>
    <p class="copy">Keystone Vantage Tenancy owns and manages over 3,700 apartments in Chicago’s best neighborhoods. All our buildings are located close to public transportation, shopping, dining, outdoor recreation, entertainment, hot spots of Chicago nightlife, and have easy access to the lakefront. From vintage to luxurious, along with the quality, convenience, and amenities you and your family want, KVT has the apartment you are looking for in Chicago.</p>
  </section>

  <div class="explore">
    <span class="rule"></span>
    <h2 class="section-title"><em>Explore</em> neighborhoods</h2>
    <span class="rule right"></span>
  </div>

  <div class="hoods">
    <figure class="hood">
      <div class="photo" role="img" aria-label="Aerial photo of Gold Coast and Old Town skyline by the lake" style="background:linear-gradient(180deg,#a9c8e2 0%,#7fa9c9 22%,#7b8286 50%,#5f9db0 80%,#2f9fae 100%)"></div>
      <figcaption class="name">Gold Coast &amp; Old Town</figcaption>
      <div class="underline"></div>
    </figure>
    <figure class="hood">
      <div class="photo" role="img" aria-label="Aerial photo of River North towers" style="background:linear-gradient(180deg,#9fc3df 0%,#3f88b2 25%,#8c8a84 55%,#6d7165 100%)"></div>
      <figcaption class="name">River North</figcaption>
      <div class="underline"></div>
    </figure>
    <figure class="hood">
      <div class="photo" role="img" aria-label="Aerial photo of Lincoln Park beach and lakefront" style="background:linear-gradient(180deg,#a9c6dc 0%,#8ea29a 25%,#5f7f55 45%,#d9ccad 62%,#3bb1b8 75%,#2d9fad 100%)"></div>
      <figcaption class="name">Lincoln Park</figcaption>
      <div class="underline"></div>
    </figure>
    <figure class="hood">
      <div class="photo" role="img" aria-label="Aerial photo of Lakeview harbor and neighborhood" style="background:linear-gradient(180deg,#a8c4dc 0%,#8c9a98 28%,#6f7f66 50%,#3f9aa8 72%,#2c8ea2 100%)"></div>
      <figcaption class="name">Lakeview</figcaption>
      <div class="underline"></div>
    </figure>
  </div>

  <section class="celebrated">
    <h2 class="section-title"><em>Chicago’s most</em> celebrated neighborhoods<br>Great neighborhoods</h2>
    <p class="copy">KVT has over 3,700 apartments to choose from in four of Chicago’s most desirable neighborhoods: Lakeview, Lincoln Park, River North and the Gold Coast. Our buildings are close to the finest bars, restaurants, entertainment and nightlife in the city.&nbsp; Not only are our buildings right in the middle of Chicago’s most vibrant and lively neighborhoods but they all have top walkability and transit ratings. Our locations make city life exciting, enjoyable and convenient.&nbsp; Fun is at your fingertips and you will be able to afford it.</p>
  </section>

  <svg class="footer" viewBox="0 0 751 97" width="751" height="97">
    <polygon points="0,0 367,0 445,97 0,97" fill="var(--red)"/>
    <polygon points="386,12 398,12 474,97 462,97" fill="var(--black)"/>
  </svg>

  <div class="contact">
    <div class="phone">
      <svg width="14" height="14" viewBox="0 0 24 24"><path d="M6.6 10.8a15.1 15.1 0 0 0 6.6 6.6l2.2-2.2c.3-.3.7-.4 1-.2 1.1.4 2.3.6 3.6.6.6 0 1 .4 1 1V20c0 .6-.4 1-1 1A17 17 0 0 1 3 4c0-.6.4-1 1-1h3.5c.6 0 1 .4 1 1 0 1.3.2 2.5.6 3.6.1.3 0 .7-.2 1z" fill="#fff"/></svg>
      773-582-6041
    </div>
    <div class="line">
      <svg width="12" height="14" viewBox="0 0 24 28"><path d="M12 0a9 9 0 0 0-9 9c0 7 9 19 9 19s9-12 9-19a9 9 0 0 0-9-9zm0 13a4 4 0 1 1 0-8 4 4 0 0 1 0 8z" fill="#fff"/></svg>
      1420 W. Harbor Lane Chicago, IL 60614
    </div>
    <div class="line">
      <svg width="13" height="13" viewBox="0 0 24 24" fill="none" stroke="#fff" stroke-width="2"><circle cx="12" cy="12" r="10"/><path d="M2 12h20M12 2c3 3 4 7 4 10s-1 7-4 10c-3-3-4-7-4-10s1-7 4-10z"/></svg>
      www.kvtresidences.example
    </div>
  </div>

  <div class="follow">
    follow us
    <div class="chips"><i></i><i></i></div>
  </div>

  <div class="partners">
    <div class="label">Our partner</div>
    <div class="badges">
      <svg class="badge" width="28" height="36" viewBox="0 0 28 36"><rect x="2" y="2" width="24" height="28" fill="#1d5ea8"/><rect x="2" y="32" width="24" height="3" fill="#1d5ea8"/></svg>
      <svg class="badge" width="46" height="32" viewBox="0 0 46 32"><rect x="0" y="0" width="46" height="32" rx="2" fill="#1d5ea8"/></svg>
      <svg class="badge" width="60" height="32" viewBox="0 0 60 32"><ellipse cx="30" cy="12" rx="18" ry="10" fill="#9a9a9a"/><rect x="2" y="25" width="56" height="7" fill="#333"/></svg>
      <svg class="badge" width="40" height="38" viewBox="0 0 40 38"><polygon points="20,2 38,14 38,30 2,30 2,14" fill="var(--black)"/><rect x="2" y="33" width="36" height="4" fill="var(--black)"/></svg>
    </div>
  </div>
</div>
</body>
</html>
```